Redesign of TaskHarbor.com website

Our website was initially developed 6+ years ago and has been maintained by several different designers. As a result, it is overly complex, inconsistent format/layout and the content is not well structured/easy to navigate

We need the site redeveloped with a more modern look and feel, simpler content structure and ability to implement new/improved tools, such as: Dynamic Forms, Sales Funnels, Landing Pages, improved metadata of our pages and posts, improved SEO/Page ranking, etc.

We currently use DealRiver CRM, Steady Reach for marketing automation and GridPilot forms. We are investigating Floxen for workflow integration which could extend to our website.

Our current website is developed in WordPress, ideally we will stick with this platform, but we’re happy to consider other CMS' if strongly recommended. We may decide to remove/consolidate some of the pages and/or content as part of this re-design.

We don't want to rebrand (ie change corporate logo, colours scheme etc) as part of this website redevelopment and it is critical that we don't lose our current Page Ranking, SEO rankings, backlink benefits, etc as part of this redevelopment.

Sites we like the feel/design of are: boardwiley.com, tallypoint.com and rankgrove.com

Target Market(s)

Corporate, Enterprise and Government B2B clients.

Coding

Coded - Design and coding required

Number of Pages Required

5+ page

Font styles to use
Sans Serif

Colors
ffffff
ec1f27

Requirements
Must have
• Must retain the majority of content on our existing website (although we may re-write some of it as part of this redesign process).
Nice to have
• See above "Project Description"
Should not have

```html
<!DOCTYPE html>
<html lang="en">
<head>
<meta charset="utf-8">
<title>TaskHarbor – Your Trusted Advisor</title>
<link href="https://fonts.googleapis.com/css2?family=Lato:wght@400;700;900&display=swap" rel="stylesheet">
<style>
:root{
  --red:#ec1f27;
  --white:#ffffff;
  --ink:#1f2229;
  --text:#4a4d55;
  --muted:#8d9099;
  --slate:#4a4e59;
  --light:#f2f2f2;
  --line:#e2e2e2;
}
*{box-sizing:border-box;margin:0;padding:0}
html,body{width:1200px;height:3555px;overflow:hidden}
body{font-family:'Lato',sans-serif;color:var(--text);background:var(--white);position:relative}
.abs{position:absolute}
section,header,footer{position:absolute;left:0;width:1200px}

/* header */
.site-header{top:0;height:69px;background:var(--white);border-bottom:1px solid var(--line)}
.brand{left:30px;top:16px;display:flex;align-items:center;gap:8px}
.brand-mark{width:32px;height:32px;border-radius:50%;background:var(--red)}
.brand-name{font-size:23px;font-weight:400;color:var(--red);line-height:1}
.brand-tag{font-size:7px;color:var(--muted);margin-left:40px;margin-top:-2px;display:block}
.main-nav{left:403px;top:28px;display:flex;gap:0}
.main-nav a{font-size:10.5px;color:var(--text);text-decoration:none;text-transform:uppercase;margin-right:19px}
.main-nav a.active{color:var(--red);border-bottom:1px solid var(--red);padding-bottom:2px}
.social{display:flex;gap:10px}
.social span{width:9px;height:9px;border-radius:50%;background:#777d87;display:block}
.social span.on{background:var(--red)}
.header-social{left:886px;top:30px}
.search-btn{left:1021px;top:22px;width:22px;height:22px;border-radius:50%;border:1px solid var(--line)}
.quote-btn{left:1055px;top:20px;width:113px;height:29px;border-radius:15px;background:var(--red);color:var(--white);font-size:10px;font-weight:900;display:flex;align-items:center;justify-content:center}

/* hero */
.hero{top:69px;height:492px;background:radial-gradient(ellipse at 70% 30%,#6a5646 0%,#3a2f28 40%,#141211 100%)}
.hero-img{inset:0}
.hero h1{width:100%;text-align:center;top:215px;font-size:31px;font-weight:900;color:var(--white);letter-spacing:.5px}
.hero p{width:100%;text-align:center;top:255px;font-size:16px;color:#e6e6e6}
.dots{display:flex;gap:10px}
.dots span{width:6px;height:6px;border-radius:50%;background:#d8d8d8}
.dots span.on{background:var(--red)}
.hero .dots{left:574px;top:470px}

/* section title */
.sec-title{width:100%;text-align:center;font-size:25px;font-weight:700;color:var(--ink)}
.sec-title i{font-style:normal;color:var(--red);font-size:16px;margin:0 12px;vertical-align:middle;letter-spacing:1px}

/* services */
.services{top:561px;height:535px;background:var(--light)}
.services .sec-title{top:68px}
.svc-card{top:136px;width:245px;height:324px;background:var(--white);box-shadow:0 2px 5px rgba(0,0,0,.07)}
.svc-head{height:98px;background:var(--slate);color:var(--white);text-align:center;padding-top:18px}
.svc-head svg{width:38px;height:38px}
.svc-head h3{font-size:15px;font-weight:700;margin-top:8px}
.svc-card.featured .svc-head{background:var(--red)}
.svc-card.faded{opacity:.35}
.svc-list{list-style:none;padding:24px 0 0 37px}
.svc-list li{font-size:9.5px;color:var(--ink);line-height:19.4px}
.svc-list li::before{content:"→";margin-right:6px;font-size:9px}
.btn{display:flex;align-items:center;justify-content:center;border-radius:16px;font-size:10.5px;color:var(--ink);border:1px solid #cfd0d4;background:var(--white)}
.btn.red{background:var(--red);color:var(--white);border-color:var(--red)}
.svc-card .btn{left:44px;top:280px;width:157px;height:31px}
.next-arrow{left:990px;top:280px;width:36px;height:36px;border-radius:50%;background:var(--slate);display:flex;align-items:center;justify-content:center}

/* about */
.about{top:1096px;height:549px;background:var(--white)}
.about-img{left:182px;top:74px;width:388px;height:399px;background:radial-gradient(circle at 50% 45%,#a84a3a 0%,#6e2620 35%,#2a1312 80%)}
.about h2{left:639px;top:112px;font-size:24px;font-weight:700;color:var(--ink);line-height:33px}
.about h2 i{font-style:normal;color:var(--red);font-size:15px;margin-left:6px}
.about h4{left:640px;top:203px;font-size:14px;font-weight:700;color:var(--ink)}
.about p{left:640px;width:380px;font-size:10.5px;line-height:17.5px;color:var(--text)}
.about .btn{left:640px;top:383px;width:121px;height:31px}

/* testimonials */
.testimonials{top:1645px;height:405px;background:linear-gradient(180deg,#1b2a35 0%,#0f1a22 55%,#16232c 100%)}
.testimonials .sec-title{top:56px;color:var(--white)}
.quote-mark{left:88px;top:180px}
.t-card{top:124px;width:410px;height:169px;background:var(--white);padding:20px 19px}
.t-card p{font-size:10.5px;line-height:17.5px;color:var(--ink)}
.t-person{left:19px;bottom:16px;display:flex;align-items:center;gap:12px}
.t-avatar{width:46px;height:46px;border-radius:50%;border:2px solid #ddd;background:var(--white)}
.t-avatar.warm{background:var(--red);border-color:#f2a3a6}
.t-name{font-size:11px;color:var(--ink)}
.t-role{font-size:8.5px;color:var(--muted);margin-top:3px}
.testimonials .dots{left:574px;top:334px}

/* news */
.news{top:2050px;height:548px;background:var(--white)}
.news .sec-title{top:68px}
.view-all{left:980px;top:80px;font-size:10px;color:var(--red);text-decoration:underline}
.news-card{top:137px;width:266px;height:338px;background:var(--white);box-shadow:0 2px 6px rgba(0,0,0,.1)}
.news-img{height:153px}
.news-body{padding:22px 19px 0}
.news-cat{font-size:9.5px;color:var(--red)}
.news-body h3{font-size:11.5px;font-weight:700;color:var(--ink);line-height:16px;margin-top:4px;height:34px}
.news-body p{font-size:10px;line-height:15px;color:var(--text);margin-top:10px}
.news-card .btn{left:19px;top:288px;width:121px;height:31px}

/* inquiry */
.inquiry{top:2598px;height:359px;background:var(--slate)}
.inquiry .sec-title{top:60px;color:var(--white)}
.field{height:28px;background:var(--white);border:1px solid #d9d9d9;font-size:9px;color:var(--muted);display:flex;align-items:center;padding-left:10px;gap:7px}
.field.area{align-items:flex-start;padding-top:10px}
.field svg{width:11px;height:11px}
.inquiry .btn{left:546px;top:270px;width:115px;height:29px;font-size:10.5px}

/* partners */
.partners{top:2957px;height:245px;background:var(--white)}
.partners .sec-title{top:58px}
.partners .view-all{top:76px;left:982px}
.logo-box{top:120px;width:152px;height:60px;border:1px solid var(--line);display:flex;align-items:center;justify-content:center;font-size:15px;font-weight:700;color:var(--slate)}
.arrow-circ{width:20px;height:20px;border-radius:50%;display:flex;align-items:center;justify-content:center}

/* footer */
.site-footer{top:3202px;height:311px;background:var(--light)}
.f-title{font-size:15px;color:var(--red)}
.f-label{font-size:9px;color:var(--red);text-transform:uppercase}
.f-text{font-size:10.5px;color:var(--ink);line-height:17px}
.f-links a{display:block;font-size:10.5px;color:var(--ink);text-decoration:none;line-height:24.5px}
.f-links a.active{color:var(--red);text-decoration:underline}
.map{left:600px;top:58px;width:418px;height:215px;background:linear-gradient(135deg,#e8efe6 0%,#dce9f2 45%,#eef0ea 100%);border:1px solid #d5d5d5}
.map-card{left:8px;top:8px;width:170px;height:62px;background:var(--white);box-shadow:0 1px 3px rgba(0,0,0,.2);padding:7px 8px}
.copyright{top:3513px;height:42px;background:var(--red);color:var(--white);font-size:10px;display:flex;align-items:center;justify-content:center}
</style>
</head>
<body>

<header class="site-header">
  <div class="abs brand">
    <span class="brand-mark"></span>
    <span class="brand-name">taskharbor</span>
  </div>
  <span class="abs brand-tag" style="left:78px;top:42px;margin:0">your trusted advisor</span>
  <nav class="abs main-nav">
    <a class="active">Home</a><a>Services</a><a>About Us</a><a>Clients</a><a>Resources</a><a>Blog</a><a>Contact Us</a>
  </nav>
  <div class="abs social header-social"><span></span><span></span><span></span><span class="on"></span><span></span></div>
  <div class="abs search-btn">
    <svg width="22" height="22" viewBox="0 0 22 22"><circle cx="10" cy="10" r="3.5" fill="none" stroke="#555" stroke-width="1.2"/><line x1="12.6" y1="12.6" x2="15" y2="15" stroke="#555" stroke-width="1.2"/></svg>
  </div>
  <div class="abs quote-btn">GET A QUOTE</div>
</header>

<section class="hero">
  <div class="abs hero-img" role="img" aria-label="Hand stopping a row of falling wooden dominoes on a table"></div>
  <h1 class="abs">BUSINESS CONTINUITY</h1>
  <p class="abs">How Robust is Your Continuity Framework?</p>
  <div class="abs dots"><span></span><span></span><span class="on"></span><span></span></div>
</section>

<section class="services">
  <h2 class="abs sec-title"><i>--</i>Services<i>--</i></h2>

  <article class="abs svc-card" style="left:182px">
    <div class="svc-head">
      <svg viewBox="0 0 40 40" fill="none" stroke="#fff" stroke-width="3"><path d="M20 6a14 14 0 0 1 13 9"/><path d="M34 24a14 14 0 0 1-9 10"/><path d="M16 34A14 14 0 0 1 6 22"/><path d="M7 14a14 14 0 0 1 5-6"/><path d="M31 10l2 5-5 1" stroke-width="2.5"/></svg>
      <h3>Resilience &amp; Continuity</h3>
    </div>
    <ul class="svc-list">
      <li>Business Continuity Management</li><li>Disaster Recovery Planning</li><li>Crisis Management</li><li>Emergency Management Planning</li><li>Workplace Health and Safety</li><li>Pandemic Response Planning</li><li>Risk Management</li>
    </ul>
    <div class="abs btn">Learn More</div>
  </article>

  <article class="abs svc-card" style="left:445px">
    <div class="svc-head">
      <svg viewBox="0 0 40 40"><path d="M20 4l13 5v10c0 9-6 15-13 18C13 34 7 28 7 19V9z" fill="#fff"/><path d="M14 20l4 4 8-8" fill="none" stroke="#4a4e59" stroke-width="3"/></svg>
      <h3>Security Management</h3>
    </div>
    <ul class="svc-list" style="padding-top:22px">
      <li>Digital Information Security Policy</li><li>Information Security Management</li><li>Cyber Security Awareness Training</li><li>Security Review and Assessment</li><li>Security Risk Management</li><li>Vulnerability Identification &amp; Testing</li><li>Penetration Testing</li>
    </ul>
    <div class="abs btn">Learn More</div>
  </article>

  <article class="abs svc-card featured" style="left:709px">
    <div class="svc-head">
      <svg viewBox="0 0 40 40"><circle cx="20" cy="20" r="11" fill="none" stroke="#fff" stroke-width="5" stroke-dasharray="5 3.6"/><circle cx="20" cy="20" r="9" fill="none" stroke="#fff" stroke-width="3"/><path d="M15 20l4 4 6-7" fill="none" stroke="#fff" stroke-width="2.5"/></svg>
      <h3>IT Services &amp; Solutions</h3>
    </div>
    <ul class="svc-list">
      <li>Keel Recovery Planner (BCM Software)</li><li>Beacon Mobile Incident Response Application</li><li>Solution Design &amp; Implementation</li><li>IT Service Management (ITSM)</li><li>IT Process &amp; Policy Development</li><li>IT Sourcing Strategy</li><li>GovCloud Migration Strategy</li>
    </ul>
    <div class="abs btn red">Learn More</div>
  </article>

  <article class="abs svc-card faded" style="left:973px;width:227px">
    <div class="svc-head" style="background:#9a9ca3">
      <svg viewBox="0 0 40 40" fill="none" stroke="#fff" stroke-width="2.5"><rect x="9" y="6" width="20" height="26"/><line x1="13" y1="13" x2="25" y2="13"/><line x1="13" y1="19" x2="25" y2="19"/><circle cx="29" cy="29" r="5"/></svg>
      <h3>Data Management</h3>
    </div>
    <ul class="svc-list">
      <li>Business Continuity Management</li><li>Disaster Recovery Planning</li><li>Crisis Management</li><li>Emergency Management Planning</li><li>Workplace Health and Safety</li><li>Pandemic Response Planning</li><li>Risk Management</li>
    </ul>
    <div class="abs btn" style="border-color:#eee">Learn More</div>
  </article>
  <div class="abs next-arrow">
    <svg width="16" height="16" viewBox="0 0 16 16"><path d="M2 8h11M9 4l4 4-4 4" fill="none" stroke="#fff" stroke-width="2"/></svg>
  </div>
</section>

<section class="about">
  <div class="abs about-img" role="img" aria-label="Hand touching a glowing digital padlock on a red background"></div>
  <h2 class="abs">How To Ensure Your Business<br>Is 100% Safe<i>--</i></h2>
  <h4 class="abs">Your business is only as strong as its weakest link.</h4>
  <p class="abs" style="top:228px">As an executive in any business, it is understandable that you want to ensure it is 100% safe, because your business is only as strong as its weakest link.</p>
  <p class="abs" style="top:296px">You know that if you have a disastrous incident it will cause irreversible damage to your company's good name, your shareholders, board of directors and industry regulators.</p>
  <div class="abs btn">Learn More</div>
</section>

<section class="testimonials">
  <div class="abs" style="inset:0" role="img" aria-label="Dark blue-tinted office with people working at desks"></div>
  <h2 class="abs sec-title"><i>--</i>Testimonials<i>--</i></h2>
  <svg class="abs quote-mark" width="64" height="56" viewBox="0 0 64 56"><path d="M2 26C2 10 10 2 24 0v10c-7 2-10 6-10 12h10v32H2zM36 26C36 10 44 2 58 0v10c-7 2-10 6-10 12h10v32H36z" fill="#ec1f27"/></svg>

  <div class="abs t-card" style="left:182px">
    <p>It was good to work with you. &nbsp;There are very few true professional organisations such as yours, in this industry. &nbsp;&nbsp;I wish you all the best and I would indeed enjoy working with you again.</p>
    <div class="abs t-person">
      <span class="t-avatar"></span>
      <div><div class="t-name">Daniel Arkwright,</div><div class="t-role">Head of Infrastructure Services – Northwind Systems</div></div>
    </div>
  </div>

  <div class="abs t-card" style="left:609px">
    <p>With all due respect, I don't see TaskHarbor in the classic consultant mould. I see you far more as 'hands-on implementation practitioners', working closely with us to define and implement real solutions to meet our business strategies</p>
    <div class="abs t-person">
      <span class="t-avatar warm"></span>
      <div><div class="t-name">Simon Prescott,</div><div class="t-role">Head of Delivery Management – Infrastructure Services, Coralnet</div></div>
    </div>
  </div>
  <div class="abs dots"><span></span><span></span><span class="on"></span><span></span></div>
</section>

<section class="news">
  <h2 class="abs sec-title"><i>--</i>The Latest News &amp; Information<i>--</i></h2>
  <span class="abs view-all">View All</span>

  <article class="abs news-card" style="left:182px">
    <div class="news-img" role="img" aria-label="Hands being washed under a running tap" style="background:linear-gradient(135deg,#8a8a86,#5f5d58 60%,#a3a09a)"></div>
    <div class="news-body">
      <div class="news-cat">Business Continuity, <span style="color:var(--text)">Pandemic</span></div>
      <h3>COVID19 – Business Recovery Phase</h3>
      <p>The following is a summary of the status updates and actions in preparing for the Recovery Phase and addressing new...</p>
    </div>
    <div class="abs btn">Learn More</div>
  </article>

  <article class="abs news-card" style="left:467px">
    <div class="news-img" role="img" aria-label="Black and white close-up of mechanical parts" style="background:linear-gradient(135deg,#2b2b2b,#777 50%,#1e1e1e)"></div>
    <div class="news-body">
      <div class="news-cat">Disaster Recovery</div>
      <h3>Decommissioning is Part of Disaster Recovery Planning</h3>
      <p>More moving parts mean more chance of failure. Replace "moving parts" by "comatose...</p>
    </div>
    <div class="abs btn">Learn More</div>
  </article>

  <article class="abs news-card" style="left:751px">
    <div class="news-img" role="img" aria-label="Digital car on a blue circuit board" style="background:linear-gradient(135deg,#5d7c95,#2f4a5e 55%,#7b9bb0)"></div>
    <div class="news-body">
      <div class="news-cat">Business Continuity</div>
      <h3>Towards Set-It-And-Forget-It Business Continuity</h3>
      <p>Few activities and operations are truly set it and forget it. Lights-out factories like...</p>
    </div>
    <div class="abs btn red">Learn More</div>
  </article>
</section>

<section class="inquiry">
  <h2 class="abs sec-title">Quick Inquiry<i style="margin-left:14px">--</i></h2>
  <div class="abs field" style="left:229px;top:118px;width:239px">
    <svg viewBox="0 0 12 12" fill="none" stroke="#666"><circle cx="6" cy="4" r="2.5"/><path d="M1.5 11.5c0-3 2-4.5 4.5-4.5s4.5 1.5 4.5 4.5"/></svg>Name</div>
  <div class="abs field" style="left:481px;top:118px;width:238px">
    <svg viewBox="0 0 12 12" fill="none" stroke="#666"><rect x="1" y="2.5" width="10" height="7"/><path d="M1 2.5l5 4 5-4"/></svg>Email</div>
  <div class="abs field" style="left:732px;top:118px;width:238px">
    <svg viewBox="0 0 12 12" fill="none" stroke="#666"><rect x="3" y="1" width="6" height="10" rx="1"/></svg>Phone</div>
  <div class="abs field area" style="left:229px;top:155px;width:741px;height:83px">
    <svg viewBox="0 0 12 12" fill="none" stroke="#666"><rect x="1.5" y="1.5" width="9" height="9"/></svg>How can we help?</div>
  <div class="abs btn red">Submit &nbsp;→</div>
</section>

<section class="partners">
  <h2 class="abs sec-title"><i>--</i>Partners<i>--</i></h2>
  <span class="abs view-all">View All</span>
  <div class="abs arrow-circ" style="left:130px;top:140px;background:#e2e2e2">
    <svg width="10" height="10" viewBox="0 0 10 10"><path d="M8 5H2M5 2L2 5l3 3" fill="none" stroke="#fff" stroke-width="1.5"/></svg>
  </div>
  <div class="abs logo-box" style="left:182px">Keystone Advisory</div>
  <div class="abs logo-box" style="left:353px">Halvern</div>
  <div class="abs logo-box" style="left:524px">Datafold</div>
  <div class="abs logo-box" style="left:695px">Stoneway Archive</div>
  <div class="abs logo-box" style="left:866px">Crestmoor</div>
  <div class="abs arrow-circ" style="left:1050px;top:140px;background:var(--red)">
    <svg width="10" height="10" viewBox="0 0 10 10"><path d="M2 5h6M5 2l3 3-3 3" fill="none" stroke="#fff" stroke-width="1.5"/></svg>
  </div>
</section>

<footer class="site-footer">
  <h3 class="abs f-title" style="left:182px;top:60px">Contact info</h3>
  <div class="abs f-label" style="left:182px;top:98px">Call us:</div>
  <div class="abs f-text" style="left:182px;top:111px;display:flex;gap:10px;align-items:flex-end">
    <svg width="10" height="10" viewBox="0 0 10 10" style="margin-bottom:4px"><path d="M2 1l2 2-1 1.5c.6 1.2 1.3 1.9 2.5 2.5L7 6l2 2-1.5 1.5C4.5 9 1 5.5.5 2.5z" fill="#ec1f27"/></svg>
    <div><div style="font-size:7.5px;line-height:9px">Tel:</div>1300-555-010</div>
    <div style="border-left:1px solid #bbb;padding-left:9px"><div style="font-size:7.5px;line-height:9px">International:</div>+61 2 5550 1234</div>
  </div>
  <div class="abs f-text" style="left:182px;top:143px;display:flex;gap:8px;align-items:center">
    <svg width="10" height="8" viewBox="0 0 10 8"><rect width="10" height="8" fill="#ec1f27"/><path d="M0 0l5 4 5-4" fill="none" stroke="#fff"/></svg>hello@taskharbor.com</div>
  <div class="abs f-label" style="left:182px;top:180px">Address:</div>
  <div class="abs f-text" style="left:182px;top:195px">Level 8, Harbour Point,<br>45 Wharf Lane, Sydney<br>NSW 2000 Australia</div>
  <div class="abs social" style="left:182px;top:268px"><span></span><span></span><span></span><span class="on"></span><span></span></div>

  <h3 class="abs f-title" style="left:449px;top:60px">Quick Link</h3>
  <nav class="abs f-links" style="left:449px;top:90px">
    <a class="active">Home</a><a>Services</a><a>About Us</a><a>Clients</a><a>Resources</a><a>Blog</a><a>Contact Us</a>
  </nav>

  <div class="abs map" role="img" aria-label="Street map of the Sydney harbour area showing the office location">
    <div class="abs map-card">
      <div style="font-size:8.5px;font-weight:700;color:var(--ink)">TaskHarbor Solutions</div>
      <div style="font-size:7px;color:var(--text);line-height:9px;margin-top:2px">Harbour Point, Level 8, 45 Wharf Ln,<br>Sydney NSW 2000</div>
      <div style="font-size:7px;color:#3b6fd1;margin-top:4px">View larger map</div>
    </div>
    <svg class="abs" style="left:396px;top:116px" width="14" height="18" viewBox="0 0 14 18"><path d="M7 0C3 0 0 3 0 7c0 5 7 11 7 11s7-6 7-11c0-4-3-7-7-7z" fill="#d93a30"/><circle cx="7" cy="7" r="2.5" fill="#fff"/></svg>
  </div>
</footer>

<div class="abs copyright" style="left:0;width:1200px">Copyright © 2021 TaskHarbor. All Rights Reserved</div>

</body>
</html>
```